Company website for an international IT business

We require a website for our business, Corvell Solutions. The business has two primary areas: Horizons, which includes two machine learning/deep learning based products and IT consultancy, which is the service we provide to other businesses.

We bridge cutting-edge research to market.

STYLING:
The site can be on single page or multi-page. This is fully open to suggestion. So long as the look and feel are consistent. Currently, we have no strong preference for colors, styles or layouts.
You can find the logo of our website in the attachment “Corvell-logo.png” and “Corvell-logo-landscape.png”.

CONTENT:
You can find the text of the website in “Website-Content.pdf”, which explains the services and products of our business. The format of the text is also open to suggestion - including breaking up the text into visually appealing sections.
We would also like to include suitable images on the website so that it does not appear to be a text-heavy page. We are happy to have placeholder images on stock image sites if needed. We are open to suggestions on placing of images

ATTACHMENT:

Industry/Entity Type

It Company

Coding

Coded - Design and coding required

Number of Pages Required

1 page

Colors

Designer to choose colors to be used in the design.

Requirements
Must have
• A full description of the requirement is in the attachment "Website-Content.pdf"
• The design must have HTML/CSS, and all resources relevant (images, fonts etc)
• We are
Nice to have
• We are open to suggestions on top of the requirement, please reach out and communicate.

```html
<!DOCTYPE html>
<html lang="en">
<head>
<meta charset="utf-8">
<title>Corvell Solutions</title>
<link rel="stylesheet" href="https://fonts.googleapis.com/css2?family=Montserrat:wght@700&family=Michroma&family=Open+Sans:wght@400;600&display=swap">
<style>
:root{
  --blue:#0b80c0;
  --blue-dark:#0a6fa8;
  --ink:#111;
  --text:#555;
  --muted:#999;
  --light:#f3f3f3;
  --footer:#343434;
  --footer-text:#cfcfcf;
  --white:#fff;
}
*{margin:0;padding:0;box-sizing:border-box}
html,body{width:697px;height:1200px;overflow:hidden;background:var(--white)}
body{position:relative;font-family:"Open Sans",Arial,sans-serif;color:var(--text)}
.abs{position:absolute}
.display{font-family:"Michroma",Verdana,sans-serif}

/* hero */
.hero{left:0;top:0;width:697px;height:394px;
  background:linear-gradient(100deg,#8c8c8c 0%,#b7b2ad 28%,#e6d8cc 50%,#ece6e2 70%,#dcdcdc 100%)}
.nav{left:0;top:0;width:697px;height:36px;background:rgba(60,60,60,.85)}
.nav a{position:absolute;top:11px;font-size:10.5px;color:#ddd;text-decoration:none}
.nav a.active{color:var(--white)}
.brand-mark{left:56px;top:12px;width:60px;height:60px;border-radius:50%;background:var(--blue);box-shadow:0 0 0 7px rgba(200,200,200,.7)}
.brand-name{left:30px;top:86px;width:112px;text-align:center;font-family:"Montserrat",sans-serif;font-weight:700;font-size:15px;color:#222;letter-spacing:1.5px}
.hero-title{right:47px;top:136px;text-align:right;font-family:"Montserrat",sans-serif;font-weight:700;font-size:35px;line-height:38px;color:var(--ink)}
.hero-sub{right:47px;top:227px;text-align:right;font-size:9.5px;line-height:14.5px;color:var(--ink);font-weight:600}

/* service band */
.band{left:0;top:394px;width:697px;height:72px;background:var(--blue)}
.band-divider{left:348px;top:404px;width:1px;height:52px;background:rgba(255,255,255,.35)}
.service-icon{width:72px;height:72px;border-radius:50%;background:var(--blue);top:357px}
.service-title{top:434px;width:300px;text-align:center;color:var(--white);font-size:14px;letter-spacing:.5px}
.card{top:466px;height:116px;background:var(--white)}
.card.left{left:46px;width:302px;box-shadow:0 4px 10px rgba(0,0,0,.12)}
.card.right{left:349px;width:348px}
.card p{position:absolute;top:16px;left:0;right:0;text-align:center;font-size:8.6px;line-height:14.5px;color:var(--text)}

/* welcome */
.welcome{left:0;top:582px;width:697px;height:212px;background:var(--light)}
.welcome h2{position:absolute;top:40px;left:0;width:697px;text-align:center;color:var(--blue);font-size:23px;font-weight:400;letter-spacing:.5px}
.welcome p{position:absolute;top:80px;left:84px;width:529px;text-align:center;font-size:8.3px;line-height:13.4px;color:var(--muted)}
.btn{left:288px;top:144px;width:121px;height:30px;background:var(--blue);color:var(--white);font-size:12px;line-height:30px;text-align:center}

/* news & testimonials */
.section-title{font-size:13.5px;color:var(--blue);letter-spacing:.3px}
.date{left:45px;width:49px;height:51px}
.date .day{height:27px;background:#d2d2d2;color:#666;font-weight:600;font-size:18px;line-height:27px;text-align:center}
.date .month{height:24px;background:var(--blue);color:var(--white);font-size:11px;line-height:24px;text-align:center}
.news-title{left:103px;font-size:10px;color:var(--ink)}
.news-desc{left:103px;font-size:8.6px;line-height:11px;color:var(--text)}
.vline{left:347px;top:822px;width:2px;height:158px;background:#ccc}
.vline::before{content:"";position:absolute;left:0;top:0;width:2px;height:26px;background:#555}
.quote{left:370px;top:852px}
.testimonial{left:372px;top:861px;width:276px;font-size:8.4px;line-height:12px;color:var(--muted);text-indent:25px}
.avatar{left:411px;top:926px;width:38px;height:38px;border-radius:50%;background:linear-gradient(#d9dde2,#aeb6bf);box-shadow:0 0 0 2px #fff,0 0 0 3px #ddd}
.person{left:461px;top:930px;font-size:10px;color:var(--blue)}
.role{left:461px;top:945px;font-size:8px;color:var(--muted)}

/* footer */
.footer{left:0;top:1010px;width:697px;height:190px;background:var(--footer)}
.f-mark{left:68px;top:1037px;width:60px;height:60px;border-radius:50%;background:var(--blue)}
.f-name{left:44px;top:1105px;width:108px;text-align:center;font-family:"Montserrat",sans-serif;font-weight:700;font-size:14px;color:var(--white);letter-spacing:1.5px}
.social{top:1131px;width:18px;height:18px;border-radius:50%;background:#6a6a6a}
.social.first{background:var(--blue)}
.f-head{top:1040px;font-size:9.5px;color:var(--white)}
.f-text{font-size:8.4px;line-height:12px;color:var(--white)}
.f-icon{left:199px}
.email-field{left:353px;top:1098px;width:115px;height:30px;background:var(--white);border-radius:3px 0 0 3px;font-size:8px;font-style:italic;color:#aaa;line-height:30px;padding-left:11px}
.email-btn{left:468px;top:1098px;width:30px;height:30px;background:var(--blue)}
.links a{position:absolute;left:507px;font-size:8.4px;color:#999;text-decoration:none}
.links a.current{color:var(--white)}
.f-rule{left:46px;top:1164px;width:606px;height:1px;background:#555}
.copyright{left:0;top:1175px;width:697px;text-align:center;font-size:10px;color:#999}
.copyright b{font-weight:400;color:var(--white)}
</style>
</head>
<body>

<div class="abs hero" role="img" aria-label="Photo of a city skyline blended with a person working on a laptop"></div>

<nav class="abs nav">
  <a class="active" style="left:252px">Home</a>
  <a style="left:313px">About Us</a>
  <a style="left:388px">Horizons</a>
  <a style="left:456px">Consultancy</a>
  <a style="left:545px">News</a>
  <a style="left:603px">Contact Us</a>
</nav>

<div class="abs brand-mark"></div>
<div class="abs brand-name">CORVELL</div>

<h1 class="abs hero-title">Business Coaching &amp;<br>Consulating For IT</h1>
<p class="abs hero-sub">Lorem Ipsum is simply dummy text of the printing and typesetting industry. Lorem Ipsum<br>has been the industry's standard dummy text ever since the 1500s</p>

<div class="abs band"></div>
<div class="abs band-divider"></div>

<div class="abs service-icon" style="left:154px">
  <svg width="72" height="72" viewBox="0 0 72 72">
    <circle cx="36" cy="36" r="30" fill="none" stroke="#fff" stroke-width="2.5"/>
    <rect x="25" y="29" width="26" height="17" rx="1.5" fill="none" stroke="#fff" stroke-width="2.5"/>
    <path d="M33 50h10M38 46v4" stroke="#fff" stroke-width="2.5"/>
    <circle cx="25" cy="25" r="4" fill="none" stroke="#fff" stroke-width="2.5"/>
    <circle cx="33" cy="20" r="3" fill="none" stroke="#fff" stroke-width="2"/>
  </svg>
</div>
<div class="abs service-icon" style="left:471px">
  <svg width="72" height="72" viewBox="0 0 72 72">
    <circle cx="36" cy="36" r="30" fill="none" stroke="#fff" stroke-width="2.5"/>
    <circle cx="27" cy="25" r="4" fill="#fff"/><circle cx="36" cy="22" r="4" fill="#fff"/><circle cx="45" cy="25" r="4" fill="#fff"/>
    <path d="M21 32h30v8h-30z" fill="#fff"/>
    <path d="M27 40v11M45 40v11M33 40v7h6v-7" stroke="#fff" stroke-width="3" fill="none"/>
  </svg>
</div>
<div class="abs display service-title" style="left:40px">HORIZONS</div>
<div class="abs display service-title" style="left:357px">CONSULTANCY</div>

<div class="abs card left"><p>Lorem Ipsum is simply dummy text of the printing<br>and typesetting industry. Lorem Ipsum has been the<br>industry's standard dummy text ever since the<br>1500.Lorem Ipsum is simply dummy text of the<br>printing and typesetting industry.</p></div>
<div class="abs card right"><p>Lorem Ipsum is simply dummy text of the printing<br>and typesetting industry. Lorem Ipsum has been the<br>industry's standard dummy text ever since the<br>1500.Lorem Ipsum is simply dummy text of the<br>printing and typesetting industry.</p></div>

<section class="abs welcome">
  <h2 class="display">WELCOME TO CORVELL</h2>
  <p>Lorem Ipsum is simply dummy text of the printing and typesetting industry. Lorem Ipsum has been the industry's standard dummy text ever since the 1500s, when an unknown printer took a galley of type and scrambled it to make a type specimen book.Lorem Ipsum is simply dummy text of the printing and typesetting industry. Lorem Ipsum has been the industry's standard dummy text ever since the 1500s, when an unknown printer took a galley of type and scrambled it to make a type specimen book.</p>
  <div class="abs btn">LEARN MORE</div>
</section>

<h3 class="abs display section-title" style="left:46px;top:822px">LATEST NEWS</h3>
<div class="abs date" style="top:853px"><div class="day">17</div><div class="month">Jan</div></div>
<div class="abs news-title" style="top:856px">Lorem Ipsum is simply dummy text</div>
<div class="abs news-desc" style="top:875px">Lorem Ipsum is simply dummy text of the printing<br>and typesetting industry...</div>
<div class="abs date" style="top:916px"><div class="day">20</div><div class="month">Jan</div></div>
<div class="abs news-title" style="top:919px">Lorem Ipsum is simply dummy text</div>
<div class="abs news-desc" style="top:938px">Lorem Ipsum is simply dummy text of the printing<br>and typesetting industry...</div>

<div class="abs vline"></div>
<h3 class="abs display section-title" style="left:361px;top:822px">TESTIMONIALS</h3>
<svg class="abs quote" width="22" height="16" viewBox="0 0 22 16" aria-hidden="true">
  <path d="M4 16L9 0h4L8 16zM12 16L17 0h4l-5 16z" fill="#777"/>
</svg>
<p class="abs testimonial">Lorem Ipsum is simply dummy text of the printing and typesetting industry. Lorem Ipsum has been the industry's standard dummy text ever since the 1500s, when an unknown printer.</p>
<svg class="abs" style="left:372px;top:910px" width="276" height="12" viewBox="0 0 276 12">
  <path d="M0 6.5H40L46 11.5L52 6.5H276" fill="none" stroke="#ccc" stroke-width="1"/>
</svg>
<div class="abs avatar" role="img" aria-label="Portrait of the client"></div>
<div class="abs display person">LOREM IPSUM</div>
<div class="abs role">CEO</div>

<footer class="abs footer"></footer>
<div class="abs f-mark"></div>
<div class="abs f-name">CORVELL</div>
<div class="abs social first" style="left:45px"></div>
<div class="abs social" style="left:66px"></div>
<div class="abs social" style="left:88px"></div>
<div class="abs social" style="left:109px"></div>
<div class="abs social" style="left:131px"></div>

<div class="abs display f-head" style="left:200px">CONTACT INFO</div>
<svg class="abs f-icon" style="top:1066px" width="13" height="13" viewBox="0 0 13 13"><path d="M1 2.5l3.5-1.5 4 1.5 3.5-1.5v9.5l-3.5 1.5-4-1.5-3.5 1.5z M4.5 1v9.5 M8.5 2.5V12" fill="none" stroke="#fff" stroke-width="1"/></svg>
<div class="abs f-text" style="left:218px;top:1064px">PO Box 4821, Harbor Lane<br>Westbridge, Norland<br>560218</div>
<svg class="abs f-icon" style="top:1110px" width="13" height="13" viewBox="0 0 13 13"><path d="M2 1.5l2.5 0 1 3-1.5 1c.8 1.7 1.8 2.7 3.5 3.5l1-1.5 3 1v2.5c-5 .5-10-4.5-9.5-9.5z" fill="none" stroke="#fff" stroke-width="1"/></svg>
<div class="abs f-text" style="left:218px;top:1110px">555 0182 376</div>
<svg class="abs f-icon" style="top:1134px" width="13" height="13" viewBox="0 0 13 13"><rect x="1" y="2.5" width="11" height="8" fill="none" stroke="#fff" stroke-width="1"/><path d="M1 2.5l5.5 4.5 5.5-4.5" fill="none" stroke="#fff" stroke-width="1"/></svg>
<div class="abs f-text" style="left:218px;top:1133px">info@corvell.com</div>

<div class="abs display f-head" style="left:354px">NEWS FEED</div>
<div class="abs f-text" style="left:354px;top:1064px">Subscribe to get news &amp; Updates of<br>our work</div>
<div class="abs email-field">E-Mail</div>
<svg class="abs email-btn" width="30" height="30" viewBox="0 0 30 30"><path d="M13 11l4 4-4 4" fill="none" stroke="#fff" stroke-width="1.8"/></svg>

<div class="abs display f-head" style="left:507px">USEFUL LINKS</div>
<nav class="links">
  <a class="current" style="top:1064px">» Home</a>
  <a style="top:1083px">» About</a>
  <a style="top:1101px">» Services</a>
  <a style="top:1119px">» Blog</a>
  <a style="top:1137px">» Contact</a>
</nav>

<div class="abs f-rule"></div>
<div class="abs copyright">© <b>CORVELL - 2018.</b> All Rights Reserved</div>

</body>
</html>
```